Smogline Atlas

Build a simple scrollable "floating" website - Website should have polished, modern look.
Domain has been bought on NameKettle and website should be setup there.
Project Brief:
https://slides.brindlepost.net/deck/7QxKp2vR9tLm4Wz8Ha3NcYe5Bj6Uf1Gd0SoVi/view?mode=shared
Input Files:
https://www.parcelvault.io/f/k3mr81zq5ex7wd2/BXKTpnLdYv9Qe_hRjG4wFs6ox?dl=0

```html
<!DOCTYPE html>
<html lang="en">
<head>
<meta charset="utf-8">
<title>Coastline Circuit – Expedition Data</title>
<link href="https://fonts.googleapis.com/css2?family=Poppins:wght@400;500;600&family=Raleway:wght@400;500;600;700&display=swap" rel="stylesheet">
<style>
:root{
  --teal:#0e7077;
  --orange:#c8420d;
  --slate:#4a4d55;
  --footer:#45484f;
  --ink:#3a3d44;
  --muted:#6d7077;
  --pale:#f3f5f8;
  --wedge:#e7eaee;
  --white:#ffffff;
}
*{box-sizing:border-box;margin:0;padding:0}
html,body{width:1200px;height:2647px;overflow:hidden;background:var(--white)}
body{position:relative;font-family:"Raleway",sans-serif;color:var(--ink)}
.abs{position:absolute}
.btn{position:absolute;display:flex;align-items:center;justify-content:center;gap:6px;font-family:"Poppins",sans-serif;font-weight:500;font-size:11px;letter-spacing:.6px;text-transform:uppercase;color:var(--white)}
.btn-orange{background:var(--orange)}
.btn-teal{background:var(--teal)}
.btn-ghost{border:1.5px solid rgba(255,255,255,.85);color:var(--white)}
.btn-white{background:var(--white);color:var(--orange)}

/* header band */
.hero-band{left:0;top:0;width:1200px;height:480px;
  background:
    radial-gradient(ellipse 300px 220px at 1080px 120px,rgba(226,222,214,.9),transparent 70%),
    radial-gradient(ellipse 260px 260px at 1120px 380px,rgba(214,196,176,.9),transparent 70%),
    radial-gradient(ellipse 320px 260px at 60px 320px,rgba(96,150,176,.85),transparent 70%),
    radial-gradient(ellipse 260px 160px at 200px 140px,rgba(140,170,150,.7),transparent 70%),
    linear-gradient(180deg,#9fb6c4 0%,#8fa9b4 45%,#c8beae 100%)}
.brand{left:155px;top:14px;display:flex;align-items:center;gap:8px;height:97px}
.brand-dot{width:22px;height:22px;border-radius:50%;background:var(--teal)}
.brand-name{font-family:"Poppins",sans-serif;font-weight:600;font-size:13px;color:var(--white)}
.nav{left:334px;top:54px;display:flex;font-family:"Poppins",sans-serif;font-size:11.5px;color:var(--white)}
.nav a{color:var(--white);text-decoration:none;margin-right:39px}
.nav a.active::before{content:"-- "}
.login{left:932px;top:48px;width:111px;height:31px}

/* hero card */
.hero-card{left:155px;top:127px;width:888px;height:401px;box-shadow:0 16px 32px rgba(0,0,0,.2);
  background:
    linear-gradient(90deg,rgba(25,30,30,.55) 0%,rgba(25,30,30,.25) 45%,transparent 70%),
    radial-gradient(ellipse 260px 150px at 700px 300px,rgba(232,232,228,.95),transparent 70%),
    radial-gradient(ellipse 200px 120px at 520px 350px,rgba(214,216,214,.9),transparent 70%),
    radial-gradient(ellipse 160px 110px at 800px 180px,rgba(205,205,200,.8),transparent 70%),
    radial-gradient(ellipse 220px 140px at 110px 330px,rgba(150,175,180,.9),transparent 70%),
    radial-gradient(ellipse 200px 110px at 120px 60px,rgba(110,140,120,.9),transparent 70%),
    radial-gradient(ellipse 320px 200px at 420px 150px,rgba(70,60,50,.9),transparent 70%),
    linear-gradient(160deg,#4e5a52 0%,#5a554c 40%,#7d7b74 70%,#a9a8a2 100%)}
.hero-title{left:231px;top:242px;width:520px;font-family:"Poppins",sans-serif;font-weight:600;font-size:29px;line-height:34px;color:var(--white)}
.hero-cta{left:231px;top:372px;width:127px;height:32px}
.dots{left:956px;top:279px;display:flex;flex-direction:column;gap:12px}
.dots span{width:9px;height:9px;border-radius:50%;background:var(--white)}
.dots span.on{background:var(--orange)}

/* expedition */
.wedge{left:0;top:480px}
.sec-title{font-family:"Poppins",sans-serif;font-weight:400;font-size:24px;color:var(--ink);display:flex;align-items:center;gap:16px}
.sec-title b{font-weight:600;color:var(--teal)}
.sec-title .rule{width:72px;height:1px;background:#8d9096}
.exp-title{left:155px;top:636px}
.exp-text{left:155px;top:700px;width:375px;font-size:14.5px;line-height:24px;color:var(--muted)}
.exp-cta{left:155px;top:867px;width:128px;height:32px}
.teal-block{left:815px;top:584px;width:228px;height:376px;background:var(--teal)}
.video{left:588px;top:625px;width:379px;height:287px;
  background:
    radial-gradient(ellipse 220px 110px at 260px 50px,rgba(70,110,55,.95),transparent 75%),
    radial-gradient(ellipse 180px 80px at 330px 120px,rgba(85,120,60,.9),transparent 75%),
    radial-gradient(ellipse 200px 90px at 250px 230px,rgba(95,90,85,.9),transparent 75%),
    radial-gradient(ellipse 140px 120px at 60px 200px,rgba(110,135,150,.9),transparent 75%),
    linear-gradient(180deg,#b9c6cf 0%,#8ea2ad 30%,#6f8590 60%,#6a675f 100%)}
.play{left:751px;top:741px}

/* data */
.data-band{left:0;top:1008px;width:1200px;height:300px;background:var(--pale)}
.centered{left:0;width:1200px;justify-content:center}
.data-title{top:1048px}
.card{position:absolute;top:1107px;height:200px;text-align:center;color:var(--white)}
.card h3{font-family:"Poppins",sans-serif;font-weight:600;font-size:17px;line-height:22px;margin-top:25px}
.card .dash{font-weight:700;font-size:14px;line-height:12px;margin:2px 0 8px}
.card p{font-size:13px;line-height:18px;padding:0 50px}
.card .btn{left:50%;transform:translateX(-50%);top:135px;width:127px;height:32px}
.card-water{left:0;width:383px;background:var(--teal)}
.card-bio{left:408px;width:383px;background:var(--orange)}
.card-report{left:815px;width:385px;background:var(--slate)}

/* trash sites */
.trash-title{top:1348px}
.tile{position:absolute}
.t1{left:155px;top:1407px;width:281px;height:159px;
  background:
    radial-gradient(ellipse 120px 50px at 80px 110px,rgba(70,140,120,.9),transparent 75%),
    radial-gradient(ellipse 120px 50px at 220px 120px,rgba(200,180,120,.9),transparent 75%),
    linear-gradient(180deg,#3f7fc4 0%,#6ea6d2 18%,#e8e4da 24%,#b6a37a 45%,#6f7f5a 100%)}
.t2{left:155px;top:1590px;width:281px;height:334px;
  background:
    radial-gradient(ellipse 120px 60px at 220px 150px,rgba(70,110,60,.9),transparent 75%),
    radial-gradient(ellipse 160px 90px at 140px 290px,rgba(40,40,42,.95),transparent 75%),
    linear-gradient(180deg,#8fb2d4 0%,#c6d6e2 30%,#7d8d92 48%,#4d5052 70%,#2e3033 100%)}
.t3{left:459px;top:1407px;width:281px;height:333px;
  background:
    radial-gradient(ellipse 120px 100px at 200px 230px,rgba(170,60,20,.6),transparent 75%),
    radial-gradient(ellipse 120px 90px at 60px 220px,rgba(180,65,22,.5),transparent 75%),
    linear-gradient(180deg,#d65a22 0%,#d3541c 60%,#da6a36 100%)}
.t4{left:459px;top:1765px;width:281px;height:159px;
  background:
    radial-gradient(ellipse 130px 40px at 140px 125px,rgba(60,110,110,.9),transparent 75%),
    linear-gradient(180deg,#c9dbe6 0%,#9fd0de 25%,#4fb8c8 50%,#8fc8c0 75%,#d9d4c0 100%)}
.t5{left:762px;top:1407px;width:281px;height:159px;
  background:
    radial-gradient(ellipse 140px 40px at 160px 120px,rgba(70,140,70,.9),transparent 75%),
    radial-gradient(ellipse 90px 30px at 60px 70px,rgba(90,90,85,.9),transparent 75%),
    linear-gradient(180deg,#c7d2dc 0%,#9eaab2 22%,#6d7570 45%,#5e7a55 75%,#7e8c6a 100%)}
.t6{left:762px;top:1590px;width:281px;height:334px;
  background:
    radial-gradient(ellipse 120px 90px at 160px 230px,rgba(90,80,70,.7),transparent 75%),
    radial-gradient(ellipse 100px 60px at 120px 300px,rgba(190,185,175,.9),transparent 75%),
    linear-gradient(180deg,#aec0d2 0%,#c7d2dc 30%,#9aa6a6 45%,#a69f90 65%,#8a8377 100%)}
.t3-caption{left:459px;top:1536px;width:281px;text-align:center;font-family:"Poppins",sans-serif;font-weight:500;font-size:14px;line-height:20px;color:var(--white)}
.t3-link{left:589px;top:1590px}
.load-more{left:544px;top:1958px;width:111px;height:32px}

/* partners */
.partners-band{left:0;top:2040px;width:1200px;height:175px;background:var(--pale)}
.partners-title{top:2064px}
.partners{left:170px;top:2128px;width:860px;display:flex;justify-content:space-between;align-items:center;height:40px}
.partner{display:flex;align-items:center;gap:8px;font-family:"Raleway",sans-serif;font-weight:700;font-size:17px;color:#2f3238}
.partner i{display:block;width:20px;height:20px;border-radius:50%;background:var(--teal)}
.partner i.sq{border-radius:0;background:var(--orange)}

/* contact */
.contact-title{left:207px;top:2256px}
.contact-intro{left:207px;top:2306px;width:385px;font-size:13px;line-height:19px;color:var(--muted)}
.info{left:207px;font-size:13px;display:flex}
.info dt{width:84px;font-weight:700;color:var(--ink)}
.info dd{color:var(--muted)}
.info dd.mail{text-decoration:underline}
.i1{top:2368px}.i2{top:2409px}.i3{top:2450px}
.social{left:205px;top:2501px;display:flex;align-items:center;gap:10px;font-size:13px;font-weight:700}
.social span.sq{width:30px;height:30px;background:#2f5fa6}
.social span.sq.b{background:#1e7bb8}
.social .label{margin-right:8px}
.field{position:absolute;left:635px;width:355px;border:1px solid #d9dce0;background:var(--white);font-size:11px;color:#a5a8ad;padding:9px 12px}
.f1{top:2264px;height:33px}.f2{top:2314px;height:33px}.f3{top:2363px;height:33px}.f4{top:2413px;height:70px}
.send{left:635px;top:2501px;width:96px;height:32px}

/* footer */
.footer{left:0;top:2582px;width:1200px;height:65px;background:var(--footer)}
.copy{left:155px;top:2606px;font-size:12px;color:#dfe1e4}
.copy u{color:var(--white)}
.to-top{left:992px;top:2582px;width:51px;height:65px;background:var(--orange);display:flex;align-items:center;justify-content:center}
</style>
</head>
<body>

<!-- header -->
<div class="abs hero-band" role="img" aria-label="Blurred coastal beach scene behind the header"></div>
<div class="abs brand"><span class="brand-dot"></span><span class="brand-name">Coastline Circuit</span></div>
<nav class="abs nav">
  <a class="active">Home</a><a>Trash Sites</a><a>Raw Data</a><a>Expedition</a><a>Supporters</a><a>Get in Touch</a>
</nav>
<div class="btn btn-orange login">
  <svg width="11" height="11" viewBox="0 0 12 12"><circle cx="6" cy="6" r="5.5" fill="#fff"/><circle cx="6" cy="4.6" r="1.9" fill="#c8420d"/><path d="M2.6 9.6c.8-1.6 2-2.2 3.4-2.2s2.6.6 3.4 2.2" fill="#c8420d"/></svg>
  Login
</div>

<!-- hero -->
<div class="abs hero-card" role="img" aria-label="Photo of a rocky shoreline covered in washed-up trash and broken styrofoam boxes"></div>
<h1 class="abs hero-title">The Data Was Recorded<br>During the 2017 Round the Coast<br>Expedition.</h1>
<div class="btn btn-teal hero-cta">Contact Us</div>
<div class="abs dots"><span></span><span class="on"></span><span></span><span></span><span></span></div>

<!-- expedition -->
<svg class="abs wedge" width="1200" height="528" viewBox="0 0 1200 528">
  <polygon points="1200,0 1200,528 580,528" fill="var(--wedge)"/>
</svg>
<h2 class="abs sec-title exp-title"><span>The <b>Expedition</b></span><span class="rule"></span></h2>
<p class="abs exp-text">In May 2017 Mara Velden and Joris Kalt completed the first successful coasteering expedition of Hong Kong Island. In 6 days they climbed, swam, scrambled and hiked the entire coastline, took 51 water samples and mapped 163 trash pollution spots</p>
<div class="btn btn-orange exp-cta">Contact Us</div>
<div class="abs teal-block"></div>
<div class="abs video" role="img" aria-label="Video still of a green headland and rocky coast with swimmers"></div>
<svg class="abs play" width="54" height="54" viewBox="0 0 54 54"><circle cx="27" cy="27" r="25" fill="none" stroke="#fff" stroke-width="2.5"/><path d="M21 17 L37 27 L21 37 Z" fill="none" stroke="#fff" stroke-width="2.5" stroke-linejoin="round"/></svg>

<!-- data & research -->
<div class="abs data-band"></div>
<h2 class="abs sec-title centered data-title"><span class="rule"></span><span>Data &amp; <b>Research</b></span><span class="rule"></span></h2>

<div class="card card-water">
  <h3>Water Pollution</h3><div class="dash">---</div>
  <p>There are many variations lorem Lorem ipsum dolor sit amet of Lorem</p>
  <div class="btn btn-ghost">&#10515; Download</div>
</div>
<div class="card card-bio">
  <h3>BioChemistry Data</h3><div class="dash">---</div>
  <p>There are many variations lorem Lorem ipsum dolor sit amet of Lorem</p>
  <div class="btn btn-white">&#10515; Download</div>
</div>
<div class="card card-report">
  <h3>Reasearch Report by Harbour<br>Open College</h3>
  <p style="margin-top:6px">There are many variations lorem Lorem ipsum dolor sit amet of Lorem</p>
  <div class="btn btn-ghost">&#10515; Download</div>
</div>

<!-- trash sites -->
<h2 class="abs sec-title centered trash-title"><span class="rule"></span><span>Trash <b>Sites</b></span><span class="rule"></span></h2>
<div class="tile t1" role="img" aria-label="Beach strewn with fishing nets and plastic debris"></div>
<div class="tile t2" role="img" aria-label="Volunteer climbing coastal rocks near a power station"></div>
<div class="tile t3" role="img" aria-label="Group of volunteers on a beach under an orange overlay"></div>
<div class="abs t3-caption">Contrary to popular belief<br>Lorem Ipsum</div>
<svg class="abs t3-link" width="22" height="22" viewBox="0 0 22 22" fill="none" stroke="#fff" stroke-width="2"><rect x="3" y="8" width="9" height="5" rx="2.5" transform="rotate(45 7.5 10.5)"/><rect x="10" y="9" width="9" height="5" rx="2.5" transform="rotate(45 14.5 11.5)"/></svg>
<div class="tile t4" role="img" aria-label="People gathering nets on a turquoise shore"></div>
<div class="tile t5" role="img" aria-label="Shoreline covered in plastic bottles"></div>
<div class="tile t6" role="img" aria-label="Volunteers kneeling to collect beach litter"></div>
<div class="btn btn-teal load-more">Load More</div>

<!-- partners -->
<div class="abs partners-band"></div>
<h2 class="abs sec-title centered partners-title"><span class="rule"></span><span>Our <b>Partners</b></span><span class="rule"></span></h2>
<div class="abs partners">
  <div class="partner"><i class="sq"></i>Far Trails Society</div>
  <div class="partner">Halvern</div>
  <div class="partner"><i></i>Tidewell Trust</div>
  <div class="partner">Northgale</div>
  <div class="partner"><i></i>Harbour Open College</div>
</div>

<!-- contact -->
<h2 class="abs sec-title contact-title"><span>Get in <b>Touch</b></span><span class="rule"></span></h2>
<p class="abs contact-intro">There are many variations of passages of Lorem Ipsum available, but the majority have suffered.</p>
<dl class="abs info i1"><dt>Address:</dt><dd>4410 Lantern Quay Rd, SL 20815</dd></dl>
<dl class="abs info i2"><dt>Phone:</dt><dd>555 - 014 - 2290</dd></dl>
<dl class="abs info i3"><dt>Email:</dt><dd class="mail">hello@coastlinecircuit.org</dd></dl>
<div class="abs social"><span class="label">Get Social:</span><span class="sq"></span><span class="sq b"></span></div>

<div class="field f1">Name*</div>
<div class="field f2">Email*</div>
<div class="field f3">Phone</div>
<div class="field f4">Message ...</div>
<div class="btn btn-orange send">
  <svg width="11" height="11" viewBox="0 0 12 12"><path d="M1 6 L11 1 L8 11 L6 7 Z" fill="#fff"/></svg>
  Send
</div>

<!-- footer -->
<div class="abs footer"></div>
<p class="abs copy">© 2017 <u>Coastline Circuit</u>. All Rights Reserved.</p>
<div class="abs to-top"><svg width="14" height="14" viewBox="0 0 14 14"><path d="M7 2 L12 8 H8.5 V12 H5.5 V8 H2 Z" fill="#fff"/></svg></div>

</body>
</html>
```